Water Bottle Design

We are launching a water bottle and need a impactful design.

Target Market(s)

health conscious hipsters

Font styles to use
Sans Serif

Requirements
Must have
• Please include the logo (included) on one side of the bottle and these words on the other side of the bottle. "It’s simple, REUSE this bottle every day. Your action, will REDUCE the amount of waste produced. SAVE your body from drinking the harmful contaminants in your water from Non-BPA plastics. HELP someone else because proceeds from your purchase will help homeless veterans.
• We’re just two dudes that like to drink water and help people. #PayItFoward"
• Use a total of two colors
• UPDATE: You do not have to use the bottle on the logo.
Nice to have
• The bottle itself is 34 ounces and looks like a normal water bottle. I will include the image in the files. We would need to be able to change the colors easily.
Should not have
• Do not use more than two colors. Colors should not be important to the design at this point.

```html
<!DOCTYPE html>
<html lang="en">
<head>
<meta charset="utf-8">
<title>Reusable Bottle – Print Layout</title>
<link href="https://fonts.googleapis.com/css2?family=Bebas+Neue&family=Raleway:wght@300&display=swap" rel="stylesheet">
<style>
  :root {
    --bottle-green: #6cc23c;
    --bottle-green-dark: #56a92b;
    --steel: #b9bcbe;
    --steel-dark: #8e9294;
    --print-white: #ffffff;
    --print-ink: #232323;
    --stage: #eef1ee;
  }
  html, body {
    margin: 0;
    padding: 0;
    overflow: hidden;
  }
  .canvas {
    position: relative;
    width: 1200px;
    height: 1034px;
    background: var(--stage);
    overflow: hidden;
  }
  .bottle {
    position: absolute;
    top: 53px;
    width: 243px;
    height: 916px;
  }
  .bottle--front { left: 337px; }
  .bottle--back { left: 641px; }
  .bottle svg {
    position: absolute;
    inset: 0;
    width: 100%;
    height: 100%;
  }
  .bottle__hashtag {
    position: absolute;
    left: 93px;
    top: 277px;
    height: 380px;
    writing-mode: vertical-rl;
    transform: rotate(180deg);
    font-family: "Bebas Neue", sans-serif;
    font-size: 70px;
    line-height: 1;
    letter-spacing: 1px;
    color: var(--print-white);
    text-align: center;
    white-space: nowrap;
  }
  .bottle__brand {
    position: absolute;
    left: 55px;
    top: 688px;
    font-family: "Raleway", sans-serif;
    font-weight: 300;
    font-size: 68px;
    line-height: 1;
    color: var(--print-ink);
    letter-spacing: -1px;
  }
  .bottle__message {
    position: absolute;
    left: 30px;
    top: 321px;
    width: 200px;
    font-family: "Bebas Neue", sans-serif;
    font-size: 19px;
    line-height: 23.5px;
    color: var(--print-ink);
  }
  .bottle__message p {
    margin: 0 0 23.5px;
  }
</style>
</head>
<body>
<div class="canvas">

  <div class="bottle bottle--front">
    <svg viewBox="0 0 243 916" aria-hidden="true">
      <defs>
        <linearGradient id="steel-front" x1="0" x2="1" y1="0" y2="0">
          <stop offset="0" stop-color="var(--steel-dark)"/>
          <stop offset="0.45" stop-color="var(--steel)"/>
          <stop offset="1" stop-color="var(--steel-dark)"/>
        </linearGradient>
      </defs>
      <rect x="79" y="0" width="85" height="72" rx="8" fill="url(#steel-front)"/>
      <path d="M84,70 L159,70 C161,160 243,220 243,310 L243,820 L0,820 L0,310 C0,220 82,160 84,70 Z" fill="var(--bottle-green)"/>
      <path d="M0,820 L243,820 L243,880 Q243,916 205,916 L38,916 Q0,916 0,880 Z" fill="url(#steel-front)"/>
    </svg>
    <div class="bottle__hashtag">#payitforward</div>
    <div class="bottle__brand">KEL</div>
  </div>

  <div class="bottle bottle--back">
    <svg viewBox="0 0 243 916" aria-hidden="true">
      <defs>
        <linearGradient id="steel-back" x1="0" x2="1" y1="0" y2="0">
          <stop offset="0" stop-color="var(--steel-dark)"/>
          <stop offset="0.45" stop-color="var(--steel)"/>
          <stop offset="1" stop-color="var(--steel-dark)"/>
        </linearGradient>
      </defs>
      <rect x="79" y="0" width="85" height="72" rx="8" fill="url(#steel-back)"/>
      <path d="M84,70 L159,70 C161,160 243,220 243,310 L243,820 L0,820 L0,310 C0,220 82,160 84,70 Z" fill="var(--bottle-green)"/>
      <path d="M0,820 L243,820 L243,880 Q243,916 205,916 L38,916 Q0,916 0,880 Z" fill="url(#steel-back)"/>
    </svg>
    <div class="bottle__message">
      <p>It is simple, reuse this<br>bottle every day</p>
      <p>Your action, will<br>reduce the amount of<br>waste produced.</p>
      <p>Save your body from<br>drinking the harmful<br>contaminants in your<br>water from non-BPA<br>plastics.</p>
      <p>Help someone else<br>because proceeds<br>from your purchase<br>will help homeless<br>veterans.</p>
    </div>
  </div>

</div>
</body>
</html>
```